Brightpath Wellness Partners

Please design a business card that is colorful but at the same time easy to read. We are based out on Miami Florida. We are a small start up healthcare company that has been in operation for 1 year. Our clients are Hospitals, Insurance companies, and Manage Care health companies. We are growing quickly and lead the niche we are in. Please make the card 2 sided on the front will be the typical info. Logo, Company Name, Persons Name, Title, Cell #, Office #, Fax#, email, website. No address. On the back we will list 5 services that we do. For example Care Transitions, Case management, Risk assessment, Utilization Review.
Target Market(s)
CEO's and COO's of hospitals and healthcare companies.
Industry/Entity Type
Healthcare

```html
<!DOCTYPE html>
<html lang="en">
<head>
<meta charset="utf-8">
<title>Brightpath Wellness Partners – Business Card</title>
<link rel="stylesheet" href="https://fonts.googleapis.com/css2?family=Roboto+Condensed:wght@400;700&display=swap">
<style>
  :root {
    --page: #d9dbdf;
    --paper: #ffffff;
    --paper-shade: #eceef1;
    --blue-light: #3d86e0;
    --blue-mid: #1f5fc8;
    --blue-deep: #133f99;
    --ink-navy: #1b2a7a;
    --ink-white: #ffffff;
    --ink-soft: #dbe7ff;
  }
  * { box-sizing: border-box; margin: 0; padding: 0; }
  html, body { width: 1200px; height: 988px; overflow: hidden; }
  body {
    background: var(--page);
    font-family: "Roboto Condensed", Arial, sans-serif;
    position: relative;
  }
  .card {
    position: absolute;
    left: 150px;
    width: 900px;
    height: 460px;
    background: var(--paper);
    overflow: hidden;
    box-shadow: 0 6px 18px rgba(0,0,0,.18);
  }
  .card--back { top: 22px; }
  .card--front { top: 506px; }
  .card__art { position: absolute; inset: 0; width: 100%; height: 100%; }

  .brand {
    position: absolute;
    display: flex;
    align-items: center;
    gap: 22px;
  }
  .brand__dot {
    width: 74px; height: 74px; border-radius: 50%;
    background: var(--blue-mid);
    flex: none;
  }
  .brand__name {
    font-weight: 700;
    font-size: 32px;
    line-height: 1.08;
    color: var(--ink-navy);
  }
  .card--back .brand { left: 48px; top: 172px; }
  .card--front .brand { left: 600px; top: 172px; }

  .services {
    position: absolute;
    left: 468px;
    top: 118px;
    width: 210px;
    color: var(--ink-white);
  }
  .services__title {
    font-weight: 700;
    font-size: 20px;
    letter-spacing: 2px;
    text-transform: uppercase;
    margin-bottom: 14px;
  }
  .services__list { list-style: none; }
  .services__item {
    font-size: 18px;
    line-height: 1.2;
    padding: 6px 0 6px 18px;
    position: relative;
  }
  .services__item::before {
    content: "";
    position: absolute;
    left: 0; top: 13px;
    width: 7px; height: 7px;
    border-radius: 50%;
    background: var(--ink-soft);
  }

  .person {
    position: absolute;
    left: 56px;
    top: 112px;
    color: var(--ink-white);
  }
  .person__name {
    font-weight: 700;
    font-size: 40px;
    letter-spacing: 1px;
    text-transform: uppercase;
  }
  .person__title {
    font-size: 17px;
    letter-spacing: 2px;
    text-transform: uppercase;
    color: var(--ink-soft);
    margin-top: 2px;
  }
  .contacts {
    position: absolute;
    left: 56px;
    top: 222px;
    display: grid;
    grid-template-columns: 200px 260px;
    row-gap: 18px;
    column-gap: 18px;
    color: var(--ink-white);
    font-size: 18px;
  }
  .contact { display: flex; align-items: center; gap: 11px; white-space: nowrap; }
  .contact svg { width: 26px; height: 26px; flex: none; }
</style>
</head>
<body>

<section class="card card--back" aria-label="Card back">
  <svg class="card__art" viewBox="0 0 900 460" preserveAspectRatio="none" aria-hidden="true">
    <defs>
      <radialGradient id="bandBack" cx="0.5" cy="0.5" r="0.7">
        <stop offset="0" stop-color="#3d86e0"/>
        <stop offset="0.6" stop-color="#1f5fc8"/>
        <stop offset="1" stop-color="#133f99"/>
      </radialGradient>
    </defs>
    <polygon points="440,0 700,0 700,460 440,460" fill="url(#bandBack)"/>
    <polygon points="760,0 900,0 900,120 830,190 760,120" fill="#eceef1"/>
    <polygon points="760,460 900,460 900,340 830,270 760,340" fill="#eceef1"/>
  </svg>
  <div class="brand">
    <span class="brand__dot"></span>
    <span class="brand__name">Brightpath<br>Wellness<br>Partners</span>
  </div>
  <div class="services">
    <div class="services__title">Our Services</div>
    <ul class="services__list">
      <li class="services__item">Care Transitions</li>
      <li class="services__item">Case Management</li>
      <li class="services__item">Risk Assessment</li>
      <li class="services__item">Utilization Review</li>
      <li class="services__item">Discharge Planning</li>
    </ul>
  </div>
</section>

<section class="card card--front" aria-label="Card front">
  <svg class="card__art" viewBox="0 0 900 460" preserveAspectRatio="none" aria-hidden="true">
    <defs>
      <radialGradient id="bandFront" cx="0.75" cy="0.3" r="0.9">
        <stop offset="0" stop-color="#3d86e0"/>
        <stop offset="0.55" stop-color="#1f5fc8"/>
        <stop offset="1" stop-color="#133f99"/>
      </radialGradient>
    </defs>
    <polygon points="0,0 560,0 560,460 0,460" fill="url(#bandFront)"/>
    <polygon points="0,0 90,0 45,45 0,45" fill="#133f99" opacity="0.6"/>
    <polygon points="830,0 900,0 900,60" fill="#eceef1"/>
    <polygon points="830,460 900,460 900,400" fill="#eceef1"/>
  </svg>

  <div class="person">
    <div class="person__name">Daniel Reyes</div>
    <div class="person__title">Managing Director</div>
  </div>

  <div class="contacts">
    <div class="contact">
      <svg viewBox="0 0 26 26" aria-hidden="true"><circle cx="13" cy="13" r="11.5" fill="none" stroke="#fff" stroke-width="1.5"/><path d="M9 7.5l2.2 2.6-1.2 1.6a8 8 0 0 0 4.3 4.3l1.6-1.2 2.6 2.2-1.3 1.7c-4.8-.6-8.8-4.6-9.4-9.4z" fill="#fff"/></svg>
      <span>C 305 555 0142</span>
    </div>
    <div class="contact">
      <svg viewBox="0 0 26 26" aria-hidden="true"><circle cx="13" cy="13" r="11.5" fill="none" stroke="#fff" stroke-width="1.5"/><rect x="7" y="9" width="12" height="8.5" fill="none" stroke="#fff" stroke-width="1.4"/><path d="M7 9l6 5 6-5" fill="none" stroke="#fff" stroke-width="1.4"/></svg>
      <span>daniel@brightpathwp.com</span>
    </div>
    <div class="contact">
      <svg viewBox="0 0 26 26" aria-hidden="true"><circle cx="13" cy="13" r="11.5" fill="none" stroke="#fff" stroke-width="1.5"/><path d="M9 7.5l2.2 2.6-1.2 1.6a8 8 0 0 0 4.3 4.3l1.6-1.2 2.6 2.2-1.3 1.7c-4.8-.6-8.8-4.6-9.4-9.4z" fill="#fff"/></svg>
      <span>O 305 555 0187</span>
    </div>
    <div class="contact">
      <svg viewBox="0 0 26 26" aria-hidden="true"><circle cx="13" cy="13" r="11.5" fill="none" stroke="#fff" stroke-width="1.5"/><circle cx="13" cy="13" r="6" fill="none" stroke="#fff" stroke-width="1.3"/><path d="M7 13h12M13 7c-3 3.5-3 8.5 0 12M13 7c3 3.5 3 8.5 0 12" fill="none" stroke="#fff" stroke-width="1.1"/></svg>
      <span>www.brightpathwp.com</span>
    </div>
    <div class="contact">
      <svg viewBox="0 0 26 26" aria-hidden="true"><circle cx="13" cy="13" r="11.5" fill="none" stroke="#fff" stroke-width="1.5"/><rect x="8.5" y="7" width="9" height="4" fill="none" stroke="#fff" stroke-width="1.3"/><rect x="7" y="11" width="12" height="6" fill="#fff"/><rect x="9" y="15" width="8" height="4.5" fill="#1f5fc8" stroke="#fff" stroke-width="1.2"/></svg>
      <span>F 305 555 0199</span>
    </div>
  </div>

  <div class="brand">
    <span class="brand__dot"></span>
    <span class="brand__name">Brightpath<br>Wellness<br>Partners</span>
  </div>
</section>

</body>
</html>
```